Business Card Design Project

I would like to have a project of business card with incorporated attachted logo elements in warm colors like: gold, yellow, brown.
We would like incorporate below information into the design
Name of the Company: Continental Hoop Invitational
Name: Dorian Pelkey
Position: Project Director
e-mail: dorian@hoopinvitational.net
mobile: +65 83147092
website: www.hoopinvitational.net
Address: 47 Marbury Lane, #06-11, Singapore 915274
There is a picture attachted which can be used as a back side of the buisness card - we would like to follow the colors theme on the front card ( with the person contact details) how ever the front card we will prefer with white background but with graphfic elements coming from logo.
Project Deadline Extended
Reason: the project has been launched on 24 of April with deadline by 24 of April by mistakes. Thats why I would like to extend the deadline.
Name: Dorian Pelkey
mobile: +65 83147092

```html
<!DOCTYPE html>
<html lang="en">
<head>
<meta charset="utf-8">
<title>Continental Hoop Invitational – Business Card</title>
<link rel="stylesheet" href="https://fonts.googleapis.com/css2?family=Gabriela&family=Open+Sans:wght@400;600&display=swap">
<style>
  :root {
    --card-yellow: #ffff00;
    --card-brown: #993d00;
    --ink-light: #ffffff;
    --ink-dark: #1a1200;
    --shadow: rgba(0, 0, 0, 0.55);
  }
  html, body {
    margin: 0;
    padding: 0;
    width: 1200px;
    height: 686px;
    overflow: hidden;
    background: var(--card-yellow);
  }
  .card {
    display: block;
    width: 1200px;
    height: 686px;
  }
  .card-background { fill: var(--card-yellow); }
  .card-band { fill: var(--card-brown); }

  .contact-name,
  .contact-role,
  .contact-mobile,
  .contact-address {
    font-family: "Open Sans", sans-serif;
    fill: var(--ink-light);
    text-anchor: end;
    filter: url(#soft-shadow);
  }
  .contact-name { font-size: 35px; font-weight: 600; }
  .contact-role { font-size: 24px; font-weight: 600; }
  .contact-mobile { font-size: 26px; font-weight: 600; }
  .contact-address { font-size: 26px; font-weight: 400; }

  .contact-web,
  .contact-email {
    font-family: "Open Sans", sans-serif;
    font-size: 23px;
    letter-spacing: 1.2px;
    fill: var(--ink-dark);
  }

  .company-name {
    font-family: "Gabriela", serif;
    font-size: 70px;
    fill: var(--ink-light);
    text-anchor: end;
    filter: url(#soft-shadow);
  }
</style>
</head>
<body>
<svg class="card" viewBox="0 0 1200 686" xmlns="http://www.w3.org/2000/svg" aria-label="Continental Hoop Invitational business card">
  <defs>
    <filter id="soft-shadow" x="-10%" y="-30%" width="120%" height="160%">
      <feDropShadow dx="2" dy="3" stdDeviation="2.5" flood-color="#000" flood-opacity="0.55"/>
    </filter>
  </defs>

  <rect class="card-background" x="0" y="0" width="1200" height="686"/>
  <polygon class="card-band" points="160,686 594,209 1200,306 1200,686"/>

  <g class="contact-block">
    <text class="contact-name" x="1149" y="74">Dorian Pelkey</text>
    <text class="contact-role" x="1149" y="123">Project Direction</text>
    <text class="contact-mobile" x="1149" y="172">M : +65 83147092</text>
  </g>

  <text class="contact-web" x="632" y="204" transform="rotate(9.1 632 204)">W : www.hoopinvitational.net</text>
  <text class="contact-email" x="192" y="650" transform="rotate(-47.7 192 650)">E  :  dorian@hoopinvitational.net</text>

  <g class="company-block">
    <text class="company-name" x="1140" y="394">Continental</text>
    <text class="company-name" x="1140" y="486">Hoop Invitational</text>
  </g>

  <text class="contact-address" x="1143" y="631">A  : 47 Marbury Lane, #06-11, Singapore 915274</text>
</svg>
</body>
</html>
```